Patent Law

Need to develop a home page for a patent lawyer.

Colors should go with logo, blues...

Company Name- Corvel Tindry, PLLC

Company Overview-

I am an Intellectual Property Lawyer and focus on patents, copyrights, trademarks, & trade secrets. I work with small businesses and start ups in the chemical and biotech industries.

Why Us-

I am small firm that can provide large-firm service at a reasonable price. I also can charge flat-fees for entreprenuers in certain practice areas.

Services-
Intellectual Property
Patents
Copyrights
Trademarks
Trade secrets
Healthcare Compliance
Elder law
Wills
Trusts

Website we like-
http://www.quarnlowtide.example/ - within industry!!
http://www.vopperhask.example/
http://dulbrickovan.example/
http://thefernwoldguides.example/

Target Market(s)

My customers will be small business, specifically small start-up companies in the chemical and biotech arena.

Industry/Entity Type

Trade

Requirements
Must have
• Colors should go with logo, blues...

```html
<!DOCTYPE html>
<html lang="en">
<head>
<meta charset="utf-8">
<title>Corvel Tindry, PLLC</title>
<link href="https://fonts.googleapis.com/css2?family=Open+Sans:wght@400;600;700&display=swap" rel="stylesheet">
<style>
:root{
  --dark:#25282b;
  --nav-a:#0b92d8;
  --nav-b:#0080c6;
  --panel-1:#0481cc;
  --panel-2:#1470b9;
  --panel-3:#0b5aa0;
  --accent:#1a8fd8;
  --brand:#1d5fb5;
  --white:#ffffff;
  --logo-text:#3d4650;
}
*{box-sizing:border-box;margin:0;padding:0}
html,body{width:1200px;height:1095px;overflow:hidden;background:var(--dark)}
body{position:relative;font-family:'Open Sans',Arial,sans-serif;color:var(--white)}
.topbar{position:absolute;left:0;top:0;width:1200px;height:59px;background:var(--dark)}
.topbar-contact{position:absolute;right:165px;top:17px;display:flex;align-items:center;gap:8px;font-size:12.5px;color:#d8dde2}
.topbar-contact .ring{width:26px;height:26px;border:2px solid var(--accent);border-radius:50%;display:flex;align-items:center;justify-content:center}
.topbar-contact .gap{width:6px}
.navband{position:absolute;left:0;top:59px;width:1200px;height:70px;background:linear-gradient(90deg,var(--nav-a),var(--nav-b))}
.mainnav{position:absolute;top:77px;left:502px;display:flex;list-style:none}
.mainnav li{font-weight:700;font-size:13.5px;height:35px;line-height:35px;padding:0 16px;border:1px solid transparent}
.mainnav li.active{border-color:var(--white)}
.logo{position:absolute;left:161px;top:0;width:227px;height:230px}
.logo-mark{position:absolute;left:246px;top:24px;width:58px;height:58px;border-radius:50%;background:var(--brand)}
.logo-name{position:absolute;left:161px;top:114px;width:227px;text-align:center;font-size:17px;font-weight:600;color:var(--logo-text);letter-spacing:.6px}
.hero{position:absolute;left:0;top:129px;width:1200px;height:784px;
  background:
    radial-gradient(ellipse 120px 150px at 62% 5%,rgba(225,220,224,.85),rgba(225,220,224,0) 100%),
    radial-gradient(ellipse 260px 260px at 96% 45%,rgba(150,70,30,.85),rgba(150,70,30,0) 100%),
    radial-gradient(ellipse 220px 260px at 3% 55%,rgba(150,105,65,.85),rgba(150,105,65,0) 100%),
    radial-gradient(ellipse 300px 240px at 48% 40%,rgba(130,55,25,.9),rgba(130,55,25,0) 100%),
    linear-gradient(180deg,#1a0f0c 0%,#2e1710 25%,#5e2a13 50%,#7a3516 75%,#5a2510 100%)}
.hero-arrow{position:absolute;top:144px}
.panels{position:absolute;left:161px;top:539px;display:flex}
.panel{position:relative;width:293px;height:293px}
.panel.why{background:var(--panel-1)}
.panel.services{background:var(--panel-2)}
.panel.contact{background:var(--panel-3)}
.panel-tab{position:absolute;left:34px;top:0}
.panel h2{position:absolute;left:100px;top:17px;font-size:25.5px;font-weight:700;letter-spacing:.3px;white-space:nowrap}
.panel-body{position:absolute;left:34px;top:83px;right:22px;font-size:12.5px;line-height:19px}
.service-list{list-style:none}
.service-list li{position:relative;padding-left:14px;margin-bottom:7.6px}
.service-list li::before{content:"";position:absolute;left:0;top:5px;border-left:5px solid var(--white);border-top:4px solid transparent;border-bottom:4px solid transparent}
.contact-list{list-style:none}
.contact-list li{position:relative;padding-left:22px;margin-bottom:8px}
.contact-list svg{position:absolute;left:0;top:3px}
.more-btn{position:absolute;left:34px;top:265px;width:92px;height:39px;border:1px solid var(--white);font-weight:700;font-size:14px;text-align:center;line-height:37px}
.why .more-btn{background:var(--panel-1)}
.services .more-btn{background:var(--panel-2)}
.contact .more-btn{background:var(--panel-3)}
.footer{position:absolute;left:0;top:913px;width:1200px;height:182px;background:var(--dark);text-align:center}
.footer-nav{margin-top:48px;font-size:12.5px}
.footer-nav span{margin:0 8px;color:#c9ced3}
.copyright{margin-top:6px;font-size:12.5px}
.social{display:flex;justify-content:center;gap:8px;margin-top:14px}
.social i{display:block;width:33px;height:33px;border:1px solid var(--white)}
.social i.filled{background:var(--accent);border-color:var(--accent)}
</style>
</head>
<body>
<header class="topbar">
  <div class="topbar-contact">
    <span class="ring"><svg width="12" height="12" viewBox="0 0 24 24"><path fill="#1a8fd8" d="M6.6 10.8a15 15 0 0 0 6.6 6.6l2.2-2.2c.3-.3.7-.4 1-.2 1.1.4 2.3.6 3.6.6.6 0 1 .4 1 1V20c0 .6-.4 1-1 1A17 17 0 0 1 3 4c0-.6.4-1 1-1h3.5c.6 0 1 .4 1 1 0 1.3.2 2.5.6 3.6.1.3 0 .7-.2 1z"/></svg></span>
    <span>+97 555-204-118</span>
    <span class="gap"></span>
    <span class="ring"><svg width="10" height="13" viewBox="0 0 10 14"><path fill="#1a8fd8" d="M5 0a5 5 0 0 0-5 5c0 3.5 5 9 5 9s5-5.5 5-9a5 5 0 0 0-5-5zm0 7a2 2 0 1 1 0-4 2 2 0 0 1 0 4z"/></svg></span>
    <span>MAP</span>
  </div>
</header>
<nav class="navband"></nav>
<ul class="mainnav">
  <li class="active">HOME</li><li>ABOUT US</li><li>SERVICES</li><li>PRACTICES</li><li>NEWS</li><li>CONTACT US</li>
</ul>

<section class="hero" role="img" aria-label="Photo of a hand holding a wooden gavel over a polished desk between old law books">
  <svg class="hero-arrow" style="left:161px" width="54" height="122" viewBox="0 0 54 122"><polyline points="53,1 2,61 53,121" fill="none" stroke="#fff" stroke-width="1.3"/></svg>
  <svg class="hero-arrow" style="left:985px" width="54" height="122" viewBox="0 0 54 122"><polyline points="1,1 52,61 1,121" fill="none" stroke="#fff" stroke-width="1.3"/></svg>
</section>

<svg class="logo" viewBox="0 0 227 230"><polygon points="0,0 227,0 227,160 113.5,230 0,160" fill="#fff"/></svg>
<span class="logo-mark"></span>
<div class="logo-name">CORVEL TINDRY, PLLC</div>

<div class="panels">
  <article class="panel why">
    <svg class="panel-tab" width="53" height="61" viewBox="0 0 53 61"><polygon points="0,0 53,0 53,47 26.5,61 0,47" fill="#fff"/><text x="26.5" y="40" text-anchor="middle" font-family="Open Sans,sans-serif" font-weight="700" font-size="32" fill="#0481cc">?</text></svg>
    <h2>WHY US</h2>
    <p class="panel-body">Lorem Ipsum is simply dummy text of the printing and typesetting industry. Lorem Ipsum has been the industry's standard dummy text ever since the 1500s, when an unknown printer took a galley of type and scrambled it to make a type specimen book. It has survived not only five centuries.</p>
    <div class="more-btn">MORE</div>
  </article>
  <article class="panel services">
    <svg class="panel-tab" width="53" height="61" viewBox="0 0 53 61"><polygon points="0,0 53,0 53,47 26.5,61 0,47" fill="#fff"/><g transform="rotate(45 26 28)" fill="#1470b9"><rect x="16" y="14" width="20" height="10" rx="2"/><rect x="23" y="24" width="6" height="18"/></g></svg>
    <h2>SERVICES</h2>
    <ul class="panel-body service-list">
      <li>Intellectual Property</li><li>Patents</li><li>Copyrights</li><li>Trademarks</li><li>Trade secrets</li><li>Healthcare Compliance</li>
    </ul>
    <div class="more-btn">MORE</div>
  </article>
  <article class="panel contact">
    <svg class="panel-tab" width="53" height="61" viewBox="0 0 53 61"><polygon points="0,0 53,0 53,47 26.5,61 0,47" fill="#fff"/><path transform="translate(16 14)" fill="#0b5aa0" d="M10.5 0A10.5 10.5 0 0 0 0 10.5C0 18 10.5 30 10.5 30S21 18 21 10.5A10.5 10.5 0 0 0 10.5 0zm0 15a4.5 4.5 0 1 1 0-9 4.5 4.5 0 0 1 0 9z"/></svg>
    <h2>CONTACT US</h2>
    <ul class="panel-body contact-list">
      <li><svg width="13" height="11" viewBox="0 0 13 11"><path fill="#fff" d="M6.5 0 0 5.5h2V11h3.5V7.5h2V11H11V5.5h2z"/></svg>CORVEL TINDRY, PLLC</li>
      <li style="line-height:25px;margin-top:-3px"><svg width="9" height="12" viewBox="0 0 10 14" style="top:7px"><path fill="#fff" d="M5 0a5 5 0 0 0-5 5c0 3.5 5 9 5 9s5-5.5 5-9a5 5 0 0 0-5-5zm0 7a2 2 0 1 1 0-4 2 2 0 0 1 0 4z"/></svg>Address :&nbsp;&nbsp; Lorem Ipsum is simply printing and typesetting industry. typesetting industry.</li>
      <li><svg width="11" height="11" viewBox="0 0 24 24"><path fill="#fff" d="M6.6 10.8a15 15 0 0 0 6.6 6.6l2.2-2.2c.3-.3.7-.4 1-.2 1.1.4 2.3.6 3.6.6.6 0 1 .4 1 1V20c0 .6-.4 1-1 1A17 17 0 0 1 3 4c0-.6.4-1 1-1h3.5c.6 0 1 .4 1 1 0 1.3.2 2.5.6 3.6.1.3 0 .7-.2 1z"/></svg>+97 555-204-118</li>
      <li><svg width="13" height="10" viewBox="0 0 13 10"><rect width="13" height="10" fill="#fff"/><polyline points="0,0 6.5,5 13,0" fill="none" stroke="#0b5aa0" stroke-width="1.3"/></svg>info@tindrylaw.example</li>
    </ul>
    <div class="more-btn">MORE</div>
  </article>
</div>

<footer class="footer">
  <div class="footer-nav">Home<span>|</span>About Us<span>|</span>Services<span>|</span>Practices<span>|</span>News<span>|</span>Contact us</div>
  <div class="copyright">Copyright © 2014 Corvel Tindry pllc. Allright Reserved</div>
  <div class="social" aria-label="Social links"><i class="filled"></i><i></i><i></i></div>
</footer>
</body>
</html>
```